KWTRM25

We want to make a full page advertisement that will be published in The Lantern magazine. It needs to be 8” x 10.75” high resolution. Our intention is to feature our upcoming attendance at KW-TRM conference in Saratoga Springs, NY in April. More information about the show can be found at https://www.kw-trm.org/saratoga-kw-trm-2025/. We want to showcase our rapid expansion and need for good quality people to join our team in the Northeast United States.

```html
<!DOCTYPE html>
<html lang="en">
<head>
<meta charset="utf-8">
<title>KW-TRM Conference Advertisement</title>
<link href="https://fonts.googleapis.com/css2?family=Oswald:wght@300;400;500;700&display=swap" rel="stylesheet">
<style>
  :root {
    --red: #e8262b;
    --red-deep: #c81f24;
    --ink: #111111;
    --panel: #262626;
    --white: #ffffff;
    --backdrop: #ececec;
    --photo-warm: #b5584a;
    --photo-dusk: #6e4548;
  }
  * { box-sizing: border-box; margin: 0; padding: 0; }
  html, body { width: 1200px; height: 616px; overflow: hidden; }
  body {
    background: var(--backdrop);
    font-family: "Oswald", "Arial Narrow", sans-serif;
    position: relative;
  }
  .ad-page {
    position: absolute;
    left: 371px; top: 0;
    width: 459px; height: 616px;
    background: var(--white);
    overflow: hidden;
  }
  .hero {
    position: absolute; left: 0; top: 0;
    width: 459px; height: 321px;
    background: var(--red);
  }
  .hero-photo {
    position: absolute; left: 0; top: 0;
    width: 459px; height: 294px;
    background:
      linear-gradient(90deg, var(--red) 0%, rgba(232,38,43,.9) 30%, rgba(232,38,43,.35) 60%, rgba(232,38,43,0) 85%),
      linear-gradient(180deg, #e49a6a 0%, var(--photo-warm) 40%, var(--photo-dusk) 100%);
  }
  .hero-shard {
    position: absolute; left: 0; top: 0;
  }
  .headline {
    position: absolute; left: 26px; top: 38px;
    color: var(--white);
    font-style: italic;
    text-transform: uppercase;
    line-height: .98;
    letter-spacing: -0.5px;
  }
  .headline .welcome { display: block; font-weight: 700; font-size: 56px; line-height: 1; }
  .headline .lead-in { display: block; font-weight: 300; font-size: 29px; margin-top: 2px; }
  .headline .org { display: block; font-weight: 700; font-size: 37px; }
  .event-band {
    position: absolute; left: 0; top: 244px;
    width: 300px; height: 50px;
    background: var(--ink);
    clip-path: polygon(0 0, 100% 0, 88% 100%, 0 100%);
    color: var(--white);
    font-style: italic;
    font-weight: 500;
    font-size: 18px;
    line-height: 1.05;
    padding: 6px 0 0 22px;
  }
  .showcase {
    position: absolute; left: 0; top: 321px;
    width: 459px; height: 238px;
    background: var(--panel);
  }
  .company {
    position: absolute; left: 0; top: 0;
    width: 184px; height: 238px;
    color: var(--white);
    text-align: center;
  }
  .company-mark {
    display: flex; align-items: center; justify-content: center; gap: 6px;
    margin-top: 32px;
  }
  .company-mark .dot {
    width: 26px; height: 26px; border-radius: 50%;
    background: var(--red);
  }
  .company-mark .name {
    font-weight: 700; font-size: 19px; color: var(--white);
    text-transform: uppercase; line-height: 1;
  }
  .company-copy {
    font-weight: 400; font-size: 12.5px; line-height: 1.22;
    margin-top: 28px;
  }
  .company-copy + .company-copy { margin-top: 16px; }
  .photo {
    position: absolute;
    background: linear-gradient(160deg, #7fa6c9 0%, #8b8a6c 45%, #a68a6a 100%);
  }
  .photo.site-dirt { background: linear-gradient(180deg, #6f9bc9 0%, #8f9a78 25%, #c7b79f 55%, #a88f74 100%); }
  .photo.site-rig { background: linear-gradient(150deg, #b7b3aa 0%, #8c7c69 60%, #6e5e4f 100%); }
  .photo.site-crew { background: linear-gradient(150deg, #6d8a5d 0%, #9a8a5e 55%, #c9a24a 100%); }
  .photo.site-field { background: linear-gradient(180deg, #556d3b 0%, #7c8b4e 45%, #8a6e55 100%); }
  .photo.site-rigs { background: linear-gradient(180deg, #3f7fd0 0%, #7aa3d8 50%, #b5a790 100%); }
  .footer-gap {
    position: absolute; left: 0; top: 559px; width: 459px; height: 14px; background: var(--white);
  }
  .contact-bar {
    position: absolute; left: 0; top: 573px;
    width: 459px; height: 32px;
    background: var(--ink);
    clip-path: polygon(0 0, 100% 0, 95% 100%, 0 100%);
    display: flex; align-items: center;
    padding-left: 22px; gap: 22px;
    color: var(--white);
    font-size: 9.5px; font-weight: 400;
  }
  .contact-item { display: flex; align-items: center; gap: 4px; white-space: nowrap; }
  .contact-item svg { width: 8px; height: 8px; fill: var(--red); }
  .corner-accent { position: absolute; right: 0; top: 561px; }
</style>
</head>
<body>
  <main class="ad-page">
    <section class="hero">
      <div class="hero-photo" role="img" aria-label="Photo of a crowded conference banquet hall with attendees at round tables"></div>
      <svg class="hero-shard" width="459" height="294" viewBox="0 0 459 294" aria-hidden="true">
        <polygon points="205,0 340,0 270,140" fill="rgba(255,255,255,.12)"/>
        <polygon points="340,0 459,0 459,60 300,150" fill="rgba(255,255,255,.06)"/>
      </svg>
      <h1 class="headline">
        <span class="welcome">Welcome</span>
        <span class="lead-in">To the home of the</span>
        <span class="org">Keywater</span>
        <span class="org">Thermal</span>
        <span class="org">Energy</span>
      </h1>
      <p class="event-band">KW-TRM Conference in<br>Saratoga Springs, NY in April</p>
    </section>

    <section class="showcase">
      <div class="company">
        <div class="company-mark">
          <span class="dot"></span>
          <span class="name">Ridgeway Thermal</span>
        </div>
        <p class="company-copy">Serving Maryland, Virginia,<br>and Southern PA. Based in<br>Laurel Maryland.</p>
        <p class="company-copy">Commercially Available in:<br>MD, PA, NJ, GA, DE, NY, CT, NC,<br>SC, MA, WV, TN</p>
      </div>
      <div class="photo site-dirt" style="left:189px;top:4px;width:95px;height:146px" role="img" aria-label="Trench with geothermal loop pipes in excavated soil"></div>
      <div class="photo site-rig" style="left:287px;top:4px;width:83px;height:63px" role="img" aria-label="Drilling rig on a construction site seen from above"></div>
      <div class="photo site-crew" style="left:373px;top:4px;width:86px;height:63px" role="img" aria-label="Crew working beside a drilling truck"></div>
      <div class="photo site-field" style="left:287px;top:70px;width:172px;height:80px" role="img" aria-label="Several drilling rigs working in a grassy field"></div>
      <div class="photo site-rigs" style="left:189px;top:153px;width:160px;height:85px" role="img" aria-label="Row of red drilling rigs under a blue sky"></div>
      <div class="photo site-rig" style="left:352px;top:153px;width:107px;height:85px" role="img" aria-label="Rig drilling inside a building foundation"></div>
    </section>

    <div class="footer-gap"></div>
    <svg class="corner-accent" width="60" height="55" viewBox="0 0 60 55" aria-hidden="true">
      <polygon points="38,0 60,0 60,55 0,55" fill="var(--red)"/>
    </svg>
    <footer class="contact-bar">
      <span class="contact-item">
        <svg viewBox="0 0 10 10"><path d="M2 0.5 L3.6 0.5 L4.2 3 L3 3.8 Q4 6 6.2 7 L7 5.8 L9.5 6.4 L9.5 8 Q9.5 9.5 8 9.5 Q1 9 0.5 2 Q0.5 0.5 2 0.5 Z"/></svg>
        (555) 0142-RTH
      </span>
      <span class="contact-item">
        <svg viewBox="0 0 10 10"><path d="M0.5 2 L9.5 2 L9.5 8.5 L0.5 8.5 Z M1 2.5 L5 5.5 L9 2.5" fill="var(--red)"/></svg>
        info@ridgewaythermal.example
      </span>
      <span class="contact-item">
        <svg viewBox="0 0 10 10"><path d="M5 0.5 Q8.5 0.5 8.5 4 Q8.5 6.5 5 9.5 Q1.5 6.5 1.5 4 Q1.5 0.5 5 0.5 Z M5 2.6 A1.4 1.4 0 1 0 5 5.4 A1.4 1.4 0 1 0 5 2.6 Z" fill-rule="evenodd"/></svg>
        48 Orchard Lane, Millbrook, NY 10001
      </span>
    </footer>
  </main>
</body>
</html>
```